依頼詳細
A社より添付の案を頂いているのですが、①グループ会社である安心感親近感をアピールしたい②メリット1のA社専用のプランを他のメリットよりも強調したいと思い、依頼をさせて頂く事となりました。
注意点、会社案内欄の箇所は空白でお願い致します。
社名を変更して今後活用したいので、パワーポイントでの納品をお願い致します。
記載項目
株式会社ZAT/03-4817-2935/https://www.za-t.jp/
サイズ
A4
ページ数
片面
希望イメージ
シンプル 複雑
単色 カラフル
暗い 明るい
日常 高級
遊び心 厳粛
未来的 伝統的
女性的 男性的
希望する色
納品ファイル
補足説明
■ 選んだ理由

社員の選定を元に選ばせて頂きました。親近感があるという意見が多かったです。

■ 提案者全員のお礼・コメント

締め切りが近い中多数のご応募頂きありがとうございます。またご機会ありましたら宜しくお願い致します。

```html
<!DOCTYPE html>
<html lang="ja">
<head>
<meta charset="UTF-8">
<title>火災保険のご案内</title>
<link href="https://fonts.googleapis.com/css2?family=Noto+Sans+JP:wght@500;700;900&display=swap" rel="stylesheet">
<style>
:root{
  --sky:#dff1fb;
  --blue:#1a8ad6;
  --blue-deep:#0f6fb8;
  --navy:#123a78;
  --red:#e8261f;
  --pink:#f4c5d2;
  --pink-line:#e26a8c;
  --orange:#f29a1f;
  --ink:#1d1d1d;
  --white:#ffffff;
}
*{margin:0;padding:0;box-sizing:border-box}
html,body{width:849px;height:1200px;overflow:hidden;background:var(--white)}
body{font-family:"Noto Sans JP",sans-serif;color:var(--ink)}
.flyer{position:relative;width:849px;height:1200px;overflow:hidden}

/* header */
.hero{position:absolute;left:0;top:0;width:849px;height:360px;background:linear-gradient(#cbe9f8,var(--sky) 60%,#f3fafe)}
.hero-house{position:absolute;left:0;top:150px;width:440px;height:210px;background:linear-gradient(#f6e2b8,#e7c78f);border-radius:6px 6px 0 0;opacity:.75}
.hero-staff{position:absolute;right:10px;top:110px;width:160px;height:190px;background:linear-gradient(#cfe3f2,#9cc3e0);border-radius:12px;opacity:.8}
.lead{position:absolute;top:22px;left:0;width:849px;text-align:center;font-size:30px;font-weight:700;color:var(--navy)}
.lead .slot{display:inline-block;width:215px;height:48px;line-height:48px;background:var(--white);border:2px solid #7fb4da;vertical-align:middle;margin-right:6px;font-size:28px;color:var(--ink);text-align:left;padding-left:16px}
.title{position:absolute;top:88px;left:0;width:849px;text-align:center;font-size:66px;font-weight:900;color:var(--red);letter-spacing:1px;-webkit-text-stroke:2px var(--white);paint-order:stroke fill;text-shadow:0 0 6px var(--white)}
.sub{position:absolute;top:180px;left:300px;width:420px;text-align:center;font-size:32px;font-weight:900;color:var(--blue-deep);line-height:1.35;text-shadow:0 0 5px var(--white),0 0 5px var(--white)}
.count{position:absolute;top:278px;left:560px;font-size:40px;font-weight:900;color:var(--red);text-shadow:0 0 5px var(--white)}
.count small{font-size:30px;color:var(--navy)}

/* merits area */
.merits{position:absolute;left:0;top:355px;width:849px;height:765px;background:linear-gradient(var(--blue),var(--blue-deep))}
.card{position:absolute;background:var(--white);border-radius:14px;box-shadow:0 4px 0 rgba(0,0,0,.15)}
.tag{position:absolute;top:-14px;background:var(--orange);color:var(--white);font-size:18px;font-weight:700;padding:3px 14px;border-radius:4px}
.tag.left{left:12px}.tag.right{right:12px}

.card-main{left:70px;top:40px;width:650px;height:195px;background:var(--white);border:4px solid var(--pink-line)}
.card-main .tag{top:-18px;font-size:22px;background:var(--red)}
.owner{text-align:center;margin-top:22px;font-size:30px;font-weight:700}
.owner .slot{display:inline-block;width:130px;height:40px;border:2px solid #999;vertical-align:middle;margin-right:10px;font-size:24px;line-height:36px}
.plan{margin:6px auto 0;width:560px;background:var(--pink);border-radius:40px;text-align:center;font-size:54px;font-weight:900;color:var(--red);line-height:70px}
.plan-note{text-align:center;font-size:24px;font-weight:700;margin-top:6px}
.plan-note small{display:block;font-size:16px;font-weight:500}
.main-staff{position:absolute;right:20px;top:0;width:100px;height:120px;background:linear-gradient(#cfe3f2,#9cc3e0);border-radius:10px}

.card-sm{width:380px;height:180px;text-align:center;padding-top:22px}
.c2{left:42px;top:255px}.c3{left:437px;top:255px}
.c4{left:42px;top:450px;height:210px}.c5{left:437px;top:450px;height:210px}
.s-small{font-size:18px;font-weight:700}
.s-big{font-size:40px;font-weight:900;color:var(--red);line-height:1.25}
.s-mid{font-size:24px;font-weight:700}
.badge{display:inline-block;background:var(--red);color:var(--white);font-size:16px;padding:2px 6px;border-radius:4px;vertical-align:middle;margin-right:6px}
.row{display:flex;align-items:center;justify-content:center;gap:12px}
.stats{font-size:15px;font-weight:700;line-height:1.5;margin-top:6px}
.c4 .s-big{font-size:62px}
.c5 .s-big{font-size:50px}
.fig{width:70px;height:80px;background:linear-gradient(#cfe3f2,#9cc3e0);border-radius:10px;flex:none}
.c4 .foot{position:absolute;left:0;bottom:0;width:100%;background:#fde8ec;border-radius:0 0 14px 14px;font-size:16px;font-weight:700;color:var(--red);line-height:34px}

.notes{position:absolute;left:0;top:1120px;width:849px;height:80px;background:var(--navy);color:var(--white);font-size:34px;font-weight:900;display:flex;align-items:center;padding-left:60px}
</style>
</head>
<body>
<div class="flyer">
  <header class="hero">
    <div class="hero-house" role="img" aria-label="家と青空のイラスト"></div>
    <div class="hero-staff" role="img" aria-label="案内する担当者たちのイラスト"></div>
    <p class="lead"><span class="slot">A社</span>の住宅購入されるお客様へ</p>
    <h1 class="title">火災保険のご案内です。</h1>
    <p class="sub">『A社』提携代理店の<br>『当社』の“専用プラン”</p>
    <p class="count">5個<small>の</small>メリット!</p>
  </header>

  <section class="merits">
    <div class="card card-main">
      <span class="tag left">メリット1</span>
      <div class="main-staff" role="img" aria-label="担当者のイラスト"></div>
      <p class="owner"><span class="slot">A社</span>オーナー様</p>
      <p class="plan">専用プラン適用!</p>
      <p class="plan-note">割安な保険料でご契約いただけます。<small>(地震保険は対象外です。)</small></p>
    </div>

    <div class="card card-sm c2">
      <span class="tag left">メリット2</span>
      <p class="s-small">ご契約時お建物資料等の</p>
      <p class="s-big"><span class="badge">簡単</span>ご提出不要!</p>
      <p class="s-mid">A社と当社で直接手続き</p>
    </div>

    <div class="card card-sm c3">
      <span class="tag right">メリット3</span>
      <div class="row"><span class="s-mid">当社は</span><span class="s-big" style="font-size:34px;line-height:1.2">火災保険<br>専門代理店!</span></div>
      <p class="stats">2019年度 お客様数約3,500件<br>2020年8月火災保険契約数約28,000件</p>
    </div>

    <div class="card card-sm c4">
      <span class="tag left">メリット4</span>
      <p class="s-big">土日祝日</p>
      <p class="s-mid">もご案内いたします!</p>
      <p class="foot">ご都合の良い日時にご案内させて頂きます。</p>
    </div>

    <div class="card card-sm c5">
      <span class="tag right">メリット5</span>
      <div class="row"><div class="fig" role="img" aria-label="担当者のイラスト"></div><p class="s-big">スピーディー</p></div>
      <p class="s-mid">なお申込み手続き!</p>
      <p class="s-small">最短で当日から補償開始!</p>
    </div>
  </section>

  <footer class="notes">注意点・会社案内欄</footer>
</div>
</body>
</html>
```